Stationary - Business Card/Letterhead and envelope design

Details for my new Stationery Design Project will be added soon. , I have two logos I am trying to decide on. I will upload the eps logos shortly. I have attached a file of what i have so far. I need urgently Business cards, but also will need a letterhead template and envelopes.

PLEASE NOTE THE DEADLINE SAYS 2 DAYS but I need business card design in LESS THAN A DAY.

thanks, Details for my new Stationery Design Project will be added soon. , I have two logos I am trying to decide on. I will upload the eps logos shortly. I have attached a file of what i have so far. I need urgently Business cards, but also will need a letterhead template and envelopes.

thanks
Updates

I have uploaded one of the logos you can work with. hopefully the other one comes soon.

details for the business card.

Marnet Dobson

Managing Director

P&K Ventures Ltd

Bda: 1-441-555-0182

Email: marnet@pkvnbda.example

web: www.pkvnbda.example

Industry/Entity Type

Business

```html
<!DOCTYPE html>
<html lang="en">
<head>
<meta charset="utf-8">
<title>P&amp;K Ventures – Business Card</title>
<link href="https://fonts.googleapis.com/css2?family=Playfair+Display:wght@700&family=Open+Sans:wght@400&display=swap" rel="stylesheet">
<style>
  :root {
    --page: #e9e6e1;
    --paper: #ffffff;
    --slate: #223d47;
    --taupe: #7b6e60;
    --ink-light: #ffffff;
    --rule: rgba(255,255,255,0.75);
  }
  * { box-sizing: border-box; margin: 0; padding: 0; }
  html, body {
    width: 1200px; height: 1023px; overflow: hidden;
    background: var(--page);
  }
  .sheet {
    width: 1200px; height: 1023px;
    display: flex; flex-direction: column; align-items: center; justify-content: center;
    gap: 60px;
  }
  .card {
    position: relative;
    width: 700px; height: 400px;
    overflow: hidden;
    box-shadow: 0 6px 18px rgba(0,0,0,0.18);
  }

  /* Front */
  .card-front { background: var(--paper); }
  .front-brand {
    position: absolute; left: 0; top: 0; width: 100%; height: 220px;
    display: flex; align-items: center; justify-content: center;
  }
  .brand-name {
    font-family: "Playfair Display", Georgia, serif;
    font-weight: 700;
    font-size: 64px;
    color: var(--taupe);
    letter-spacing: 0.5px;
  }
  .front-details {
    position: absolute; left: 0; bottom: 0; width: 100%; height: 180px;
    background: var(--slate);
  }
  .person {
    position: absolute; left: 44px; bottom: 38px;
  }
  .person-name {
    font-family: "Playfair Display", Georgia, serif;
    font-weight: 700;
    font-size: 28px;
    color: var(--taupe);
  }
  .person-title {
    font-family: "Open Sans", Arial, sans-serif;
    font-size: 15px;
    color: var(--ink-light);
    margin-top: 2px;
  }
  .divider {
    position: absolute; left: 372px; top: 0; width: 1px; height: 120px;
    background: var(--rule);
  }
  .contacts {
    position: absolute; left: 400px; top: 22px;
    list-style: none;
    font-family: "Open Sans", Arial, sans-serif;
    font-size: 15px;
    color: var(--ink-light);
  }
  .contacts li { display: flex; align-items: center; gap: 10px; line-height: 27px; }
  .contacts svg { width: 11px; height: 11px; flex: none; }

  /* Back */
  .card-back { background: var(--slate); }
  .back-tab {
    position: absolute; right: 0; top: 0; width: 22px; height: 280px;
    background: var(--taupe);
  }
  .back-brand {
    position: absolute; inset: 0;
    display: flex; align-items: center; justify-content: center;
  }
  .card-back .brand-name { color: var(--ink-light); font-size: 76px; }
</style>
</head>
<body>
<main class="sheet">
  <section class="card card-front" aria-label="Business card front">
    <div class="front-brand">
      <span class="brand-name">P&amp;K Ventures</span>
    </div>
    <div class="front-details">
      <div class="person">
        <p class="person-name">Marnet Dobson</p>
        <p class="person-title">Managing Director</p>
      </div>
      <span class="divider"></span>
      <ul class="contacts">
        <li>
          <svg viewBox="0 0 12 12" aria-hidden="true"><path d="M3 1 L5 3.5 L4 4.8 Q5.2 7 7.2 8 L8.5 7 L11 9 L9.6 11 Q4.5 10.5 1 2.4 Z" fill="#ffffff"/></svg>
          1-441-555-0182
        </li>
        <li>
          <svg viewBox="0 0 12 12" aria-hidden="true"><rect x="0.5" y="2.5" width="11" height="7" fill="#ffffff"/><path d="M0.5 2.5 L6 6.5 L11.5 2.5" fill="none" stroke="#223d47" stroke-width="1"/></svg>
          marnet@pkvnbda.example
        </li>
        <li>
          <svg viewBox="0 0 12 12" aria-hidden="true"><circle cx="6" cy="6" r="5.2" fill="none" stroke="#ffffff" stroke-width="1.2"/><ellipse cx="6" cy="6" rx="2.2" ry="5.2" fill="none" stroke="#ffffff" stroke-width="1"/><path d="M0.8 6 H11.2" stroke="#ffffff" stroke-width="1"/></svg>
          www.pkvnbda.example
        </li>
      </ul>
    </div>
  </section>

  <section class="card card-back" aria-label="Business card back">
    <span class="back-tab"></span>
    <div class="back-brand">
      <span class="brand-name">P&amp;K Ventures</span>
    </div>
  </section>
</main>
</body>
</html>
```